Billboard design for a small town Oral Surgeon

We are getting several billboards and need a design that highlights the doctors photo, and bullet points of what he does. Our business name is extremely long, so it’s a challenge to figure out how to do this. Maybe just use our logo? Open to ideas.
The logo can be shortened as designer sees fit, meaning we can drop the tag line. Important info to include:
Doctors name is Tobin Marek
The highlighted bullet points are:
•Implants
•wisdom teeth
•Jaw Surgery
•facial trauma
The goal of this billboard is to let our community know that they have an option here in Ada, our town. Many still drive to the city a couple hours away not knowing they now have an option here at home. Having a hard time finding examples of what I have in mind, so hoping this will get us going. I want it as “non-busy” as possible, so no unnecessary lines or anything that competes with the information we are trying to get across.

Target Market(s)

Everyone in town, just trying to spread the word that we are here

Industry/Entity Type

Medical/surgical (oral surgery)

Font styles to use
Sans Serif

Colors
0094D4
00A9DD
6FCCEA
C7EBF8
E9F6FB

Requirements
Must have
• *New note** Due to location of billboard, I prefer the photo of doctor to be on the left side. Must look neat and professional. Must highlight what we do.
Nice to have
• Our colors are a blue-green with silver, against black or white, but I’m flexible on this, I don’t necessarily need the colors highlighted. I’m also flexible on font style, just needs to be easy to read.
Should not have
• Distracting graphics, should not look like a dental office. That’s an issue we have is people thinking we are another dental office, we do not do any general dentistry, it’s surgery only.

```html
<!DOCTYPE html>
<html lang="en">
<head>
<meta charset="utf-8">
<title>Riverbend Oral &amp; Maxillofacial Surgery – Billboard</title>
<link rel="stylesheet" href="https://fonts.googleapis.com/css2?family=Questrial&family=Roboto+Condensed:wght@500&family=Montserrat:wght@400;600&display=swap">
<style>
  :root {
    --backdrop: #262626;
    --teal: #2190a9;
    --teal-deep: #1a7489;
    --navy: #1e2a3e;
    --white: #ffffff;
    --ink: #1c1c1c;
    --silver: #9c9c9c;
    --silver-light: #c9c9c9;
  }
  html, body {
    margin: 0;
    padding: 0;
    width: 963px;
    height: 1200px;
    overflow: hidden;
    background: var(--backdrop);
  }
  .billboard {
    position: absolute;
    left: 30px;
    top: 449px;
    width: 903px;
    height: 301px;
    display: block;
  }
  .practice-name {
    font-family: "Questrial", sans-serif;
    font-size: 34px;
    fill: var(--ink);
    letter-spacing: -0.3px;
  }
  .service-label {
    font-family: "Roboto Condensed", sans-serif;
    font-weight: 500;
    font-size: 38px;
    fill: var(--white);
  }
  .logo-name {
    font-family: "Questrial", sans-serif;
    font-size: 24px;
    fill: var(--teal);
  }
  .contact-phone {
    font-family: "Montserrat", sans-serif;
    font-weight: 600;
    font-size: 27px;
    fill: var(--white);
  }
  .contact-web {
    font-family: "Montserrat", sans-serif;
    font-weight: 400;
    font-size: 20px;
    fill: var(--white);
  }
</style>
</head>
<body>
<svg class="billboard" viewBox="0 0 1096 365" xmlns="http://www.w3.org/2000/svg" aria-label="Riverbend Oral and Maxillofacial Surgery billboard">
  <defs>
    <linearGradient id="portrait-tone" x1="0" y1="0" x2="0" y2="1">
      <stop offset="0" stop-color="#2a8aa0"/>
      <stop offset="0.55" stop-color="#d9b7a3"/>
      <stop offset="1" stop-color="#1e2a3e"/>
    </linearGradient>
  </defs>

  <!-- panels -->
  <rect class="panel-white" x="0" y="0" width="1096" height="365" fill="var(--white)"/>
  <polygon class="panel-teal" points="0,0 357,0 421,365 0,365" fill="var(--teal)"/>
  <polygon class="contact-band" points="415,305 1096,305 1096,365 421,365" fill="var(--silver)"/>

  <!-- doctor portrait placeholder -->
  <g class="doctor-portrait" role="img" aria-label="Portrait photo of Dr. Tobin Marek in a dark suit and red tie">
    <path d="M80,365 L80,130 Q80,20 160,20 Q240,20 240,130 L240,225 L327,265 L327,365 Z" fill="url(#portrait-tone)" opacity="0.9"/>
  </g>

  <!-- practice mark -->
  <g class="practice-mark">
    <circle cx="384" cy="184" r="92" fill="var(--white)"/>
    <text class="logo-name" x="384" y="192" text-anchor="middle">Riverbend</text>
  </g>

  <!-- practice name -->
  <text class="practice-name" x="547" y="77">RIVERBEND ORAL</text>
  <text class="practice-name" x="547" y="117">&amp; MAXILLOFACIAL SURGERY</text>

  <!-- services -->
  <g class="service-pill">
    <rect x="497" y="155" width="209" height="45" rx="22.5" fill="var(--teal)"/>
    <circle cx="520" cy="177.5" r="16" fill="none" stroke="var(--white)" stroke-width="3"/>
    <text class="service-label" x="547" y="193" textLength="131" lengthAdjust="spacingAndGlyphs">IMPLANTS</text>
  </g>
  <g class="service-pill">
    <rect x="497" y="217" width="257" height="44" rx="22" fill="var(--teal)"/>
    <circle cx="520" cy="239" r="16" fill="none" stroke="var(--white)" stroke-width="3"/>
    <text class="service-label" x="547" y="254" textLength="191" lengthAdjust="spacingAndGlyphs">JAW SURGERY</text>
  </g>
  <g class="service-pill">
    <rect x="777" y="155" width="272" height="45" rx="22.5" fill="var(--teal)"/>
    <circle cx="800" cy="177.5" r="16" fill="none" stroke="var(--white)" stroke-width="3"/>
    <text class="service-label" x="827" y="193" textLength="205" lengthAdjust="spacingAndGlyphs">WISDOM TEETH</text>
  </g>
  <g class="service-pill">
    <rect x="777" y="217" width="272" height="44" rx="22" fill="var(--teal)"/>
    <circle cx="800" cy="239" r="16" fill="none" stroke="var(--white)" stroke-width="3"/>
    <text class="service-label" x="827" y="254" textLength="204" lengthAdjust="spacingAndGlyphs">FACIAL TRAUMA</text>
  </g>

  <!-- contact -->
  <g class="contact-phone-icon">
    <circle cx="456" cy="334" r="15" fill="var(--teal)"/>
    <path d="M449,326 q2,-2 4,0 l2,3 q1,2 -1,3 q1,4 5,6 q1,-2 3,-1 l3,2 q2,2 0,4 q-3,3 -8,0 q-7,-5 -9,-11 q-1,-4 1,-6 z" fill="var(--white)"/>
  </g>
  <text class="contact-phone" x="475" y="343">(580) 555-0147</text>
  <line x1="716" y1="320" x2="716" y2="348" stroke="var(--white)" stroke-width="2"/>
  <g class="contact-web-icon" fill="none" stroke="var(--white)" stroke-width="1.6">
    <circle cx="753" cy="334" r="15" fill="var(--teal)" stroke="none"/>
    <circle cx="753" cy="334" r="9"/>
    <ellipse cx="753" cy="334" rx="4" ry="9"/>
    <line x1="744" y1="334" x2="762" y2="334"/>
    <line x1="746" y1="329" x2="760" y2="329"/>
    <line x1="746" y1="339" x2="760" y2="339"/>
  </g>
  <text class="contact-web" x="775" y="341" textLength="298" lengthAdjust="spacingAndGlyphs">www.riverbendoralsurgery.com</text>
</svg>
</body>
</html>
```